Electrical Contractors Business Card Design

I need a business card design for an electrical contracting business. A theme I was thinking of is the BE of Brightway Electrical both facing each other ie the second E is back to front and maybe each horizontal part of the E's are a different colours of the internal wires of TPS cable. The top would be blue(representing the sky), the middle green(representing the grass) and the lower would be brown(representing below the earth) (neutral,earth and active). And coming out of the back of each E going to each side of the business card would be the white outer sheath of TPS cable. I would like a big part of the card to be a very bright emerald flourescent green and maybe silver for the top half. the message I would like to send is that of an environmentally friendly, ethical business that delivers quality sevice on time.

Target Market(s)

40 to 80 year old home owners

Industry/Entity Type

Electrical

Contact Information for Business Card

Tom Keller
Brightway Electrical
EC 274381
Mob: 0417 592 064

```html
<!DOCTYPE html>
<html lang="en">
<head>
<meta charset="UTF-8">
<title>Brightway Electrical – Business Card</title>
<link rel="stylesheet" href="https://fonts.googleapis.com/css2?family=Barlow:wght@400&family=Barlow+Condensed:wght@600&display=swap">
<style>
  :root {
    --page-bg: #ffffff;
    --silver: #e3e7ec;
    --sheath-white: #ffffff;
    --emerald: #6a9d62;
    --wire-blue: #1e6fb8;
    --text-light: #ffffff;
  }
  * { margin: 0; padding: 0; box-sizing: border-box; }
  html, body {
    width: 1200px;
    height: 900px;
    overflow: hidden;
    background: var(--page-bg);
  }
  .card {
    position: absolute;
    left: 65px;
    top: 117px;
    width: 1075px;
    height: 648px;
    background: var(--emerald);
    overflow: hidden;
  }
  .card__sky {
    position: absolute;
    left: 0; top: 0;
    width: 100%;
    height: 221px;
    background: var(--silver);
  }
  .card__sheath {
    position: absolute;
    left: 0; top: 221px;
    width: 100%;
    height: 60px;
    background: var(--sheath-white);
  }
  .brand__mark {
    position: absolute;
    left: 127px;
    top: 145px;
    width: 233px;
    height: 216px;
    background: var(--wire-blue);
  }
  .brand__name {
    position: absolute;
    left: 390px;
    top: 218px;
    font-family: "Barlow Condensed", sans-serif;
    font-weight: 600;
    font-size: 64px;
    line-height: 66px;
    letter-spacing: 1px;
    color: var(--emerald);
    white-space: nowrap;
  }
  .contact {
    position: absolute;
    left: 649px;
    top: 378px;
    font-family: "Barlow", sans-serif;
    font-weight: 400;
    font-size: 40px;
    line-height: 55px;
    color: var(--text-light);
    list-style: none;
  }
</style>
</head>
<body>
  <div class="card">
    <div class="card__sky"></div>
    <div class="card__sheath"></div>
    <div class="brand__mark"></div>
    <div class="brand__name">BRIGHTWAY ELECTRICAL</div>
    <ul class="contact">
      <li class="contact__name">Tom Keller</li>
      <li class="contact__licence">EC 274381</li>
      <li class="contact__mobile">M: 0417 592 064</li>
    </ul>
  </div>
</body>
</html>
```